Business Card and Letterhead Design Project

We need a business card template and letterhead designed for our new business.
Business Card
The information on the business card will be:
Logo
"slogan" - A whole new way to 401k
Person's Name
Title
Phone Number
Email Address
Website
We strive to make everything SIMPLE so please keep that in mind.
If you want to design something that would go on an odd shaped business card, that is fine, we are up for any ideas.
The Letterhead would have:
logo
business address
phone
fax
website
Here is a link to our logo files: http://qlinkvo.example/7Rm2TzP
we can provide the winning designer with higher quality files if needbe.

```html
<!DOCTYPE html>
<html lang="en">
<head>
<meta charset="utf-8">
<title>Sproutly – Business Card and Letterhead</title>
<link href="https://fonts.googleapis.com/css2?family=Arimo:ital,wght@0,400;0,700;1,400&display=swap" rel="stylesheet">
<style>
  :root {
    --canvas: #ffffff;
    --paper: #dcdcdc;
    --card-front: #d9d9d9;
    --ink: #2f2f2f;
    --ink-soft: #4a4a4a;
    --leaf: #79b32b;
    --leaf-deep: #5a9150;
    --leaf-mid: #69a63a;
    --clay: #c9620f;
    --clay-light: #f2e4d6;
  }
  * { box-sizing: border-box; margin: 0; padding: 0; }
  html, body { width: 1200px; height: 717px; overflow: hidden; background: var(--canvas); }
  body { position: relative; font-family: "Arimo", Arial, sans-serif; color: var(--ink); }

  .brand { display: flex; align-items: center; gap: 6px; }
  .brand-mark { border-radius: 50%; border: 2px solid var(--leaf); flex: none; }
  .brand-name { font-weight: 700; color: var(--ink-soft); letter-spacing: -0.02em; line-height: 1; }
  .slogan { font-weight: 700; color: var(--ink); }

  /* Business card front */
  .card-front {
    position: absolute; left: 98px; top: 77px; width: 217px; height: 134px;
    background: var(--card-front); box-shadow: 0 1px 3px rgba(0,0,0,.25);
  }
  .card-front .brand { position: absolute; left: 14px; top: 13px; }
  .card-front .brand-mark { width: 18px; height: 18px; }
  .card-front .brand-name { font-size: 19px; }
  .card-front .slogan { position: absolute; left: 40px; top: 36px; font-size: 6px; }
  .card-person { position: absolute; left: 40px; top: 57px; font-size: 6.5px; line-height: 1.35; }
  .card-person .person-name { font-weight: 700; }
  .card-person .person-title { color: var(--leaf); font-style: italic; }
  .contact { font-size: 6.5px; line-height: 1.6; }
  .contact .label { color: var(--leaf); font-weight: 700; }
  .contact .web { color: var(--leaf); font-style: italic; }
  .card-front .contact { position: absolute; left: 40px; top: 87px; }

  /* Business card back */
  .card-back {
    position: absolute; left: 98px; top: 245px; width: 217px; height: 134px;
    background: linear-gradient(90deg, var(--leaf-mid) 0%, var(--leaf-mid) 55%, var(--leaf-deep) 100%);
    box-shadow: 0 1px 3px rgba(0,0,0,.25);
  }
  .card-back .emblem {
    position: absolute; left: 83px; top: 41px; width: 52px; height: 52px;
    border-radius: 50%; background: rgba(140, 200, 80, .45);
  }
  .card-back .plant-note { position: absolute; right: 6px; bottom: 5px; font-size: 5px; font-weight: 700; color: #fff; }

  /* Planting illustration */
  .planting {
    position: absolute; left: 66px; top: 443px; width: 303px; height: 154px;
    background: linear-gradient(180deg, var(--clay-light) 0%, #e7a66f 55%, var(--clay) 100%);
  }
  .caption { position: absolute; left: 55px; top: 617px; width: 342px; font-size: 11.4px; line-height: 1.3; color: var(--ink); }
  .caption strong { font-size: 12.6px; }

  /* Letterheads */
  .sheet {
    position: absolute; width: 565px; height: 640px; background: var(--paper);
    box-shadow: 0 1px 4px rgba(0,0,0,.2);
  }
  .sheet-first { left: 421px; top: 99px; }
  .sheet-second { left: 586px; top: 309px; }

  .sheet-first .brand { position: absolute; left: 50px; top: 94px; }
  .sheet-first .brand-mark { width: 20px; height: 20px; }
  .sheet-first .brand-name { font-size: 21px; }
  .sheet-first .slogan { position: absolute; left: 79px; top: 118px; font-size: 6.5px; }
  .sender { position: absolute; left: 459px; top: 110px; font-size: 6.5px; line-height: 1.45; }
  .sender .contact { margin-top: 8px; line-height: 1.45; }

  .letter-body { position: absolute; width: 362px; font-size: 6.4px; line-height: 11.4px; }
  .letter-body p + p { margin-top: 11px; }
  .sheet-first .letter-body { left: 52px; top: 228px; }
  .sheet-second .letter-body { left: 58px; top: 151px; }
  .signature { margin-top: 11px; }

  .sheet-second .brand-mark { position: absolute; left: 53px; top: 108px; width: 20px; height: 20px; }
</style>
</head>
<body>

  <section class="card-front" aria-label="Business card, front">
    <div class="brand"><span class="brand-mark"></span><span class="brand-name">sproutly</span></div>
    <p class="slogan">A whole new way to 401k</p>
    <div class="card-person">
      <p class="person-name">Daniel Reed Hollis</p>
      <p class="person-title">CEO Sproutly</p>
    </div>
    <div class="contact">
      <p><span class="label">T</span> 000 · 000 · 000</p>
      <p><span class="label">E</span> dan@sproutly.example</p>
      <p class="web">www.sproutly.example</p>
    </div>
  </section>

  <section class="card-back" aria-label="Business card, back">
    <span class="emblem"></span>
    <p class="plant-note">Plant me!</p>
  </section>

  <div class="planting" role="img" aria-label="Illustration: a seed-paper card planted in a clay pot, watered, then growing into a blue flower"></div>

  <p class="caption"><strong>The business cards</strong> are made out of seed paper, when planted it grows a flower. This idea links directly to your brands name and concept of blooming giving the customer an extra experience not just a business card.</p>

  <section class="sheet sheet-first" aria-label="Letterhead, first page">
    <div class="brand"><span class="brand-mark"></span><span class="brand-name">sproutly</span></div>
    <p class="slogan">A whole new way to 401k</p>
    <address class="sender" style="font-style:normal">
      <p>Harlow Street 17,<br>08021 Valencia, Spain.</p>
      <div class="contact">
        <p><span class="label">T</span> 000 · 000 · 000</p>
        <p><span class="label">E</span> dan@sproutly.example</p>
        <p class="web">www.sproutly.example</p>
      </div>
    </address>
    <div class="letter-body">
      <p>Dear Martin,</p>
      <p>We are pleased to share the first look at our retirement planning service. Our aim is to make saving for the future clear, calm and simple for every member of your team. Each plan is built around your goals, your timeline and the level of risk that feels right to you. We review fees openly, keep paperwork light and send short updates every quarter so nothing is left unclear. Our advisors are ready to answer questions by phone or email, and we will gladly meet in person to walk through the details. Thank you for considering us as your partner for long term growth.</p>
      <p class="signature">Daniel Reed Hollis</p>
    </div>
  </section>

  <section class="sheet sheet-second" aria-label="Letterhead, following page">
    <span class="brand-mark"></span>
    <div class="letter-body">
      <p>We are pleased to share the first look at our retirement planning service. Our aim is to make saving for the future clear, calm and simple for every member of your team. Each plan is built around your goals, your timeline and the level of risk that feels right to you. We review fees openly, keep paperwork light and send short updates every quarter so nothing is left unclear. Our advisors are ready to answer questions by phone or email, and we will gladly meet in person to walk through the details. Thank you for considering us as your partner for long term growth.</p>
      <p>Daniel Reed Hollis founded the firm to help small companies offer better plans without the usual cost or confusion. Today our team supports hundreds of savers across the country with tools that are easy to read and easy to use. We believe a good plan should fit on a single page and grow with you year after year.<br>Getting started takes only a few minutes. Send us a short list of your staff and current plan details, and we will prepare a clear comparison within one week. There is no charge for this review and no obligation to continue.<br>We look forward to hearing from you soon and to helping your people build a brighter future.</p>
    </div>
  </section>

</body>
</html>
```